" Plataforma on line que realiza o gerenciamento de ligações telefônicas de empresas. Os clientes visualizam as informações através de relatórios e gráficos e áudios referentes ao seu banco de dados. "

```html
<!DOCTYPE html>
<html lang="pt-BR">
<head>
<meta charset="utf-8">
<title>Ligara – Cartões de visita</title>
<link href="https://fonts.googleapis.com/css2?family=Montserrat:wght@400;600&display=swap" rel="stylesheet">
<style>
  :root {
    --canvas: #a9a9a9;
    --black: #000000;
    --white: #ffffff;
    --band: #d4d4d4;
    --ink: #5a5a5a;
    --logo-light: #ffffff;
    --logo-grey: #9a9a9a;
  }
  * { margin: 0; padding: 0; box-sizing: border-box; }
  html, body { width: 1200px; height: 1200px; overflow: hidden; }
  body { background: var(--canvas); position: relative; font-family: "Montserrat", sans-serif; }

  .card { position: absolute; }
  .card--front { background: var(--black); }
  .card--back { background: var(--white); }
  .card--wide { width: 408px; height: 224px; }
  .card--square { width: 276px; height: 280px; }

  .brand {
    position: absolute; display: flex; flex-direction: column; align-items: center;
    left: 50%; top: 50%; transform: translate(-50%, -50%);
  }
  .brand__row { display: flex; align-items: center; gap: 8px; }
  .brand__dot { width: 20px; height: 20px; border-radius: 50%; background: currentColor; }
  .brand__name { font-size: 34px; font-weight: 600; letter-spacing: 0.5px; line-height: 1; }
  .brand__tag { font-size: 6.5px; font-weight: 600; letter-spacing: 2.2px; margin-top: 4px; text-transform: uppercase; }
  .brand--light { color: var(--logo-light); }
  .brand--grey { color: var(--logo-grey); }
  .brand--small .brand__name { font-size: 22px; }
  .brand--small .brand__dot { width: 13px; height: 13px; }
  .brand--small .brand__row { gap: 5px; }
  .brand--small .brand__tag { font-size: 4.5px; letter-spacing: 1.5px; margin-top: 3px; }

  .back__band { position: absolute; left: 160px; right: 0; top: 36px; height: 29px; background: var(--band); }
  .back__name { position: absolute; left: 42px; top: 39px; font-size: 11px; color: var(--ink); }
  .back__role { position: absolute; left: 64px; top: 58px; font-size: 8px; color: var(--ink); }
  .contact { position: absolute; left: 38px; top: 120px; list-style: none; }
  .contact li { display: flex; align-items: center; gap: 9px; height: 24px; font-size: 7.5px; color: var(--ink); }
  .contact svg { width: 10px; height: 10px; fill: var(--ink); }
  .back__brand { left: auto; right: 36px; top: 150px; transform: translateY(-50%); }
</style>
</head>
<body>
  <svg width="0" height="0" style="position:absolute">
    <defs>
      <symbol id="i-phone" viewBox="0 0 10 10"><path d="M2 0.5 3.6 2.4 2.8 3.6Q4 6 6.4 7.2L7.6 6.4 9.5 8 8.4 9.5Q4.5 9.5 0.5 5.5 0.5 1.6 2 0.5Z"/></symbol>
      <symbol id="i-mail" viewBox="0 0 10 10"><path d="M0.5 2h9v6h-9z M1.2 2.6 5 5.6 8.8 2.6" fill="none" stroke="#5a5a5a" stroke-width="0.9"/></symbol>
      <symbol id="i-web" viewBox="0 0 10 10"><circle cx="5" cy="5" r="4.3" fill="none" stroke="#5a5a5a" stroke-width="0.9"/><path d="M0.7 5h8.6M5 0.7q-2.6 4.3 0 8.6M5 0.7q2.6 4.3 0 8.6" fill="none" stroke="#5a5a5a" stroke-width="0.7"/></symbol>
      <symbol id="i-pin" viewBox="0 0 10 10"><path d="M5 0.3A3.3 3.3 0 0 0 1.7 3.6C1.7 6 5 9.7 5 9.7S8.3 6 8.3 3.6A3.3 3.3 0 0 0 5 0.3Zm0 4.7a1.4 1.4 0 1 1 0-2.8 1.4 1.4 0 0 1 0 2.8Z"/></symbol>
    </defs>
  </svg>

  <!-- Row 1 -->
  <section class="card card--front card--wide" style="left:144px;top:84px">
    <div class="brand brand--light"><div class="brand__row"><span class="brand__dot"></span><span class="brand__name">Ligara</span></div><span class="brand__tag">Inteligência empresarial</span></div>
  </section>
  <section class="card card--back card--wide" style="left:624px;top:84px">
    <div class="back__band"></div>
    <p class="back__name">Rafael Lima</p>
    <p class="back__role">Cargo</p>
    <ul class="contact">
      <li><svg><use href="#i-phone"/></svg>(11) 9000-1234</li>
      <li><svg><use href="#i-mail"/></svg>rafael@ligara.com.br</li>
      <li><svg><use href="#i-web"/></svg>www.ligara.com.br</li>
      <li><svg><use href="#i-pin"/></svg>Endereço</li>
    </ul>
    <div class="brand brand--grey brand--small back__brand"><div class="brand__row"><span class="brand__dot"></span><span class="brand__name">Ligara</span></div><span class="brand__tag">Inteligência empresarial</span></div>
  </section>

  <!-- Row 2 -->
  <section class="card card--front card--wide" style="left:144px;top:355px">
    <div class="brand brand--light"><div class="brand__row"><span class="brand__dot"></span><span class="brand__name">Ligara</span></div><span class="brand__tag">Inteligência empresarial</span></div>
  </section>
  <section class="card card--back card--wide" style="left:624px;top:355px">
    <div class="back__band"></div>
    <p class="back__name">Helena Souza</p>
    <p class="back__role">Cargo</p>
    <ul class="contact">
      <li><svg><use href="#i-phone"/></svg>(11) 9000-5678</li>
      <li><svg><use href="#i-mail"/></svg>helena@ligara.com.br</li>
      <li><svg><use href="#i-web"/></svg>www.ligara.com.br</li>
      <li><svg><use href="#i-pin"/></svg>Endereço</li>
    </ul>
    <div class="brand brand--grey brand--small back__brand"><div class="brand__row"><span class="brand__dot"></span><span class="brand__name">Ligara</span></div><span class="brand__tag">Inteligência empresarial</span></div>
  </section>

  <!-- Row 3 -->
  <section class="card card--front card--wide" style="left:144px;top:608px">
    <div class="brand brand--light"><div class="brand__row"><span class="brand__dot"></span><span class="brand__name">Ligara</span></div><span class="brand__tag">Inteligência empresarial</span></div>
  </section>
  <section class="card card--back card--wide" style="left:624px;top:608px">
    <div class="back__band"></div>
    <p class="back__name">Caio Prado</p>
    <p class="back__role">Cargo</p>
    <ul class="contact">
      <li><svg><use href="#i-phone"/></svg>(11) 9000-9012</li>
      <li><svg><use href="#i-mail"/></svg>caio@ligara.com.br</li>
      <li><svg><use href="#i-web"/></svg>www.ligara.com.br</li>
      <li><svg><use href="#i-pin"/></svg>Endereço</li>
    </ul>
    <div class="brand brand--grey brand--small back__brand"><div class="brand__row"><span class="brand__dot"></span><span class="brand__name">Ligara</span></div><span class="brand__tag">Inteligência empresarial</span></div>
  </section>

  <!-- Square cards -->
  <section class="card card--front card--square" style="left:156px;top:890px">
    <div class="brand brand--light"><div class="brand__row"><span class="brand__dot"></span><span class="brand__name">Ligara</span></div><span class="brand__tag">Inteligência empresarial</span></div>
  </section>
  <section class="card card--back card--square" style="left:475px;top:890px">
    <div class="brand brand--grey"><div class="brand__row"><span class="brand__dot"></span><span class="brand__name">Ligara</span></div><span class="brand__tag">Inteligência empresarial</span></div>
  </section>
  <section class="card card--back card--square" style="left:787px;top:890px">
    <div class="brand brand--grey"><div class="brand__row"><span class="brand__dot"></span><span class="brand__name">Ligara</span></div><span class="brand__tag">Inteligência empresarial</span></div>
  </section>
</body>
</html>
```